Australian Wine Online Sales website

We need to build an online presence for our export wine business 'Lanmeixo' that targets Australian wine to the Chinese consumer. Ideally the website will have look and feel of Western elegance and sophistication, but also build the personal brand of the Owner. The Chinese buying segment like to connect with their personal buyer in Australia. They need to see and feel authenticity and trust of the proprietor of the online sales business. We have direct access to the Australia wine producers, vineyards and the story of each wine producer and their products. This needs to be matched with a pictorial sales-cart so the owner can upload, describe and price the products, and the customer can read/browse and purchase items in the cart, possibly with provision for shipping costs, promotions, vouchers, referral/affiliate commission, and cross-links to social and business pages such as Talkora, Qinlu and Streamly & Snapvista, multiple payments terms and currencies (including Paxio and TalkoraPay). The site must have a feel of young, sophisticated elegance - not 'Old World' but 'New World' adventure and opportunity. Our physical presence is in Western Australia. A list of wineries in this region and their wines are found here: https://en.vinoreference.org/wiki/Register_of_cellars_in_Western_Australia
Updates

Hello Everyone, I appreciated all your participation and hard work. Maybe I didn't explain very well. It is very hard for me to comment on every of your design, because they are all similar and basic, not the design I like. We want to be an online shop has a smaller range of wines at the beginning, mainly are Australian wines. I have a hand drawing the design I preferred for the home page, to attract customers to know our wine collection better. I will try to upload them today. Great thanks to all of you. Margaret

Target Market(s)

Chinese young adult wine consumer

Industry/Entity Type

Winery

Coding

Coded - Design and coding required

Number of Pages Required

3 page

Font styles to use
Serif
Sans Serif
Decorative

Colors

Designer to choose colors to be used in the design.

Requirements
Must have
• Wine pictures and pictures of Margaret Zhou
• Shopping Cart
• sophisticated New World Australia feel
Nice to have
• Map links to winery locations
Should not have
• Poor taste

```html
<!DOCTYPE html>
<html lang="en">
<head>
<meta charset="utf-8">
<title>Lanmeixo — Australian Wine</title>
<link href="https://fonts.googleapis.com/css2?family=Dosis:wght@500;600;700;800&family=Open+Sans:wght@400;600;700&display=swap" rel="stylesheet">
<style>
:root{
  --blue:#1da1e2;
  --blue-deep:#1a6fb5;
  --navy:#1b5a97;
  --ink:#2b3440;
  --muted:#7b8794;
  --sky:#d8ecf8;
  --sky-soft:#eef6fb;
  --panel:#4e8dc5;
  --white:#ffffff;
  --gold:#f2a516;
  --wine:#6d1b2a;
}
*{margin:0;padding:0;box-sizing:border-box}
html,body{width:1200px;height:4592px;overflow:hidden}
body{position:relative;background:var(--white);font-family:"Open Sans",sans-serif;color:var(--ink);font-size:13px}
.abs{position:absolute}
.heading{font-family:"Dosis",sans-serif;font-weight:700;text-transform:uppercase;letter-spacing:.5px}
.eyebrow{font-family:"Dosis",sans-serif;font-size:12px;letter-spacing:2px;color:var(--blue);text-transform:uppercase;font-weight:600}
.section-title{font-size:26px;color:var(--blue-deep)}
.center{left:0;width:1200px;text-align:center}
.title-rule{width:40px;height:2px;background:var(--blue);margin:6px auto 0}

/* header */
.topbar{top:0;left:0;width:1200px;height:86px;background:var(--white)}
.contact-mini{left:162px;top:24px;font-size:12px;color:var(--ink);line-height:16px}
.contact-mini svg{vertical-align:middle;margin-right:6px}
.cart{left:955px;top:33px;font-size:11px;color:var(--ink)}
.search{left:1028px;top:33px}
.navbar{top:86px;left:0;width:1200px;height:27px;background:var(--blue)}
.nav-item{position:absolute;top:0;height:27px;line-height:27px;font-family:"Dosis",sans-serif;font-weight:700;font-size:11px;color:var(--white);text-transform:uppercase;letter-spacing:.5px}
.nav-item.active{background:var(--white);color:var(--blue);padding:0 12px}
.brand{left:536px;top:0;width:128px;height:122px;background:var(--blue);border-radius:0 0 64px 64px;display:flex;align-items:center;justify-content:center}
.brand-ring{width:96px;height:96px;border-radius:50%;border:2px solid var(--white);display:flex;align-items:center;justify-content:center;font-family:"Dosis",sans-serif;font-weight:700;color:var(--white);font-size:17px;letter-spacing:.5px}

/* hero */
.hero{top:113px;left:0;width:1200px;height:484px;background:linear-gradient(100deg,#c6e2f5 0%,#b3d8f1 45%,#8ec4e9 100%)}
.swatches{left:36px;top:10px}
.swatch{width:26px;height:26px;margin-bottom:6px}
.hero-title{left:162px;top:193px;font-family:"Dosis",sans-serif;font-weight:800;font-size:27px;line-height:32px;color:var(--white);text-transform:uppercase}
.hero-sub{left:162px;top:262px;font-size:13px;color:var(--white)}
.pill{display:inline-flex;align-items:center;gap:10px;background:var(--white);border-radius:20px;padding:4px 4px 4px 16px;font-size:11px;color:var(--ink)}
.pill .dot{width:20px;height:20px;border-radius:50%;background:var(--blue);display:flex;align-items:center;justify-content:center}
.hero-cta{left:162px;top:300px}
.hero-photo{left:600px;top:0;width:600px;height:484px;border-radius:260px 0 0 260px;background:radial-gradient(ellipse 55% 70% at 38% 55%,#e9c9ad 0%,#b98f72 22%,#5a3c2c 48%,#2b1d17 72%,#3a2a22 100%)}

/* top wines */
.wine-band{top:765px;left:0;width:1200px;height:322px;display:flex}
.wine-feature{width:240px;height:322px;background:var(--sky-soft);position:relative}
.wine-panel{flex:1;height:322px;background:linear-gradient(180deg,#6aa2d3 0%,#4e8dc5 60%,#3f7db7 100%);position:relative;border-left:1px solid rgba(255,255,255,.25);text-align:center}
.bottle-slot{position:absolute;left:50%;transform:translateX(-50%);bottom:0;width:74px;height:250px;border-radius:30px 30px 6px 6px;background:linear-gradient(90deg,#244f7a 0%,#3d74a8 45%,#2a5a88 100%)}
.feature-slot{position:absolute;left:50%;transform:translateX(-50%);top:30px;width:70px;height:250px;border-radius:28px 28px 6px 6px;background:linear-gradient(90deg,#3e0e18 0%,#8a2838 45%,#4a1320 100%)}
.panel-label{position:absolute;left:0;width:100%;top:140px;font-family:"Dosis",sans-serif;font-weight:700;font-size:13px;color:var(--white);z-index:2}
.panel-label small{display:block;font-size:9px;font-weight:600;letter-spacing:1px;opacity:.85;margin-top:2px}
.arrow-btn{width:28px;height:28px;border:1px solid var(--blue-deep);display:flex;align-items:center;justify-content:center;background:var(--white)}
.arrow-btn.filled{background:var(--blue-deep)}

/* about */
.about{top:1230px;left:0;width:1200px;height:515px;background:linear-gradient(100deg,#ffffff 0%,#e6f2fa 55%,#c6e1f3 100%)}
.about-photo{left:720px;top:0;width:480px;height:515px;background:radial-gradient(ellipse 60% 55% at 85% 40%,#e3c3a8 0%,#caa386 35%,rgba(198,225,243,.6) 70%,rgba(230,242,250,0) 100%)}
.about-text{left:162px;top:138px;width:600px;font-size:11px;line-height:18px;color:var(--muted)}
.goal{width:290px}
.goal-icon{width:44px;height:44px;border-radius:50%;border:1px solid #9fb3c4;display:flex;align-items:center;justify-content:center;float:left;margin-right:14px}
.goal h4{font-family:"Dosis",sans-serif;font-size:13px;color:var(--ink);font-weight:700;text-transform:uppercase;margin-bottom:4px}
.goal p{font-size:10px;line-height:15px;color:var(--muted);overflow:hidden}

/* shop */
.filter{width:60px;height:60px;border-radius:50%;border:3px solid;display:flex;align-items:center;justify-content:center;text-align:center;font-size:8px;line-height:10px;color:var(--ink);background:var(--white)}
.product{width:200px;height:336px;text-align:center}
.product.hover{box-shadow:0 4px 18px rgba(0,0,0,.15);background:var(--white)}
.product-shot{position:absolute;left:50%;transform:translateX(-50%);top:18px;width:52px;height:196px;border-radius:20px 20px 5px 5px}
.badge{position:absolute;left:0;top:0;font-family:"Dosis",sans-serif;font-size:10px;font-weight:700;color:var(--white);padding:3px 8px}
.product-name{position:absolute;left:0;width:100%;top:236px;font-size:12px}
.product-price{position:absolute;left:0;width:100%;top:264px;font-family:"Dosis",sans-serif;font-size:16px;font-weight:700;color:var(--ink)}
.stars{position:absolute;left:0;width:100%;top:290px;color:var(--gold);font-size:13px;letter-spacing:1px}
.stars .off{color:#cfd6dc}

/* team */
.team{top:2394px;left:0;width:1200px;height:520px;background:linear-gradient(180deg,#1c9be0 0%,#168ed6 100%)}
.member{width:210px;height:292px;background:var(--white);text-align:center}
.member-photo{position:absolute;left:10px;top:10px;width:190px;height:200px;background:radial-gradient(ellipse 50% 60% at 50% 42%,#d9b59b 0%,#c9a68c 35%,#e3e6e9 62%,#cfd5db 100%)}
.member-name{position:absolute;left:0;width:100%;top:228px;font-family:"Dosis",sans-serif;font-weight:700;font-size:15px;color:var(--ink)}
.member-role{position:absolute;left:0;width:100%;top:252px;font-size:9px;letter-spacing:1px;color:var(--muted)}
.round-arrow{width:40px;height:26px;border-radius:13px;display:flex;align-items:center;justify-content:center}

/* blog */
.blog{width:276px;height:281px;background:var(--white);box-shadow:0 3px 14px rgba(0,0,0,.08)}
.blog-img{position:absolute;left:0;top:0;width:276px;height:180px;background:linear-gradient(180deg,#2c1f1a 0%,#4a1e22 35%,#7a2a2a 60%,#c48a4e 85%,#e0b070 100%)}
.blog-caption{position:absolute;left:0;top:180px;width:100%;height:50px;background:var(--blue);padding:9px 14px;font-size:11px;font-weight:600;color:var(--white);line-height:15px}
.blog-title{position:absolute;left:14px;top:196px;width:250px;font-size:11px;font-weight:600;color:var(--blue-deep);line-height:15px}
.blog-meta{position:absolute;left:14px;top:248px;font-size:9px;color:var(--muted)}
.blog-meta span{margin-right:16px}

/* affiliate */
.affiliate{top:3484px;left:0;width:1200px;height:174px;background:var(--sky)}
.affiliate p{position:absolute;left:162px;top:50px;width:610px;font-size:12px;line-height:20px;color:#4a6a88}
.affiliate .btn{position:absolute;left:796px;top:61px;background:var(--white);border-radius:20px;padding:5px 5px 5px 14px;font-size:10px;display:flex;align-items:center;gap:8px}

/* contact */
.map{top:4065px;left:0;width:600px;height:481px;background:linear-gradient(135deg,#eef0e6 0%,#e2e8d8 40%,#cfe3f1 70%,#b8d6ee 100%)}
.office{top:4065px;left:600px;width:600px;height:481px;background:var(--navy)}
.contact-card{top:3771px;left:285px;width:682px;height:346px;background:var(--white);box-shadow:0 6px 24px rgba(0,0,0,.12);z-index:3}
.contact-card .intro{position:absolute;left:0;width:100%;top:38px;text-align:center;font-size:14px;line-height:20px;color:#4d5965}
.field{position:absolute;height:28px;border:1px solid #dfe3e7;font-size:10px;color:var(--muted);padding:7px 10px}
.captcha{position:absolute;left:30px;top:304px;width:150px;height:32px;background:#f6f7f8;border:1px solid #dcdfe2}
.captcha i{position:absolute;left:9px;top:8px;width:14px;height:14px;border:1px solid #aeb4ba;background:var(--white)}
.captcha b{position:absolute;right:8px;top:6px;width:20px;height:20px;border-radius:50%;background:#9fb3c8}
.submit{position:absolute;left:217px;top:309px;width:392px;height:33px;background:var(--blue);color:var(--white);font-family:"Dosis",sans-serif;font-weight:700;font-size:12px;text-align:center;line-height:33px;letter-spacing:1px}
.office h3{position:absolute;left:86px;top:158px;font-family:"Dosis",sans-serif;font-size:24px;font-weight:700;color:var(--white)}
.office h3 span{color:#6ec3f2}
.office .label{position:absolute;left:86px;font-family:"Dosis",sans-serif;font-size:12px;font-weight:700;color:var(--white);text-transform:uppercase;letter-spacing:.5px}
.office .line{position:absolute;left:86px;font-size:10px;line-height:15px;color:#cfe0f0}
.socials{position:absolute;left:86px;top:326px;display:flex;gap:18px}
.socials span{font-size:10px;color:var(--white);display:flex;align-items:center;gap:5px}
.socials span::before{content:"";width:8px;height:8px;border-radius:50%;background:#6ec3f2}
.copyright{top:4546px;left:0;width:1200px;height:46px;line-height:46px;text-align:center;font-size:10px;color:var(--muted);background:var(--white)}
</style>
</head>
<body>

<header class="abs topbar">
  <div class="abs contact-mini">
    <div><svg width="10" height="10" viewBox="0 0 10 10"><path d="M2 1l2 2-1 1.5c.6 1.2 1.3 1.9 2.5 2.5L7 6l2 2-1.5 1.5C4.5 9.5.5 5.5.5 2.5z" fill="#2b3440"/></svg>+61 8 5550 0142</div>
    <div style="padding-left:16px;font-size:10px;color:#7b8794">hello@lanmeixo.example</div>
  </div>
  <div class="abs cart"><svg width="12" height="12" viewBox="0 0 12 12" style="vertical-align:middle;margin-right:4px"><path d="M1 2h2l1.5 6h6l1-4.5H4" stroke="#2b3440" fill="none"/><circle cx="5" cy="10.5" r="1" fill="#2b3440"/><circle cx="9.5" cy="10.5" r="1" fill="#2b3440"/></svg>CART(0)</div>
  <div class="abs search"><svg width="12" height="12" viewBox="0 0 12 12"><circle cx="5" cy="5" r="3.8" stroke="#2b3440" stroke-width="1.5" fill="none"/><path d="M8 8l3 3" stroke="#2b3440" stroke-width="1.5"/></svg></div>
</header>
<nav class="abs navbar">
  <span class="nav-item active" style="left:172px">Home</span>
  <span class="nav-item" style="left:246px">All Wines</span>
  <span class="nav-item" style="left:325px">About Us</span>
  <span class="nav-item" style="left:402px">Shop Extract</span>
  <span class="nav-item" style="left:710px">Members</span>
  <span class="nav-item" style="left:790px">Blogs &amp; News</span>
  <span class="nav-item" style="left:892px">Affiliate</span>
  <span class="nav-item" style="left:974px">Contact Us</span>
</nav>
<div class="abs brand" style="z-index:4"><div class="brand-ring">Lanmeixo</div></div>

<section class="abs hero">
  <div class="abs hero-photo" role="img" aria-label="Photo of Margaret Zhou selecting a bottle from a wine cellar rack"></div>
  <div class="abs swatches">
    <div class="swatch" style="background:#fff"></div>
    <div class="swatch" style="background:#c9ced3"></div>
    <div class="swatch" style="background:#3a3f45"></div>
    <div class="swatch" style="background:#6b7077"></div>
    <div class="swatch" style="background:#1a6fb5"></div>
    <div class="swatch" style="background:#1da1e2"></div>
    <div class="swatch" style="background:#a8d6f2"></div>
  </div>
  <h1 class="abs hero-title">Enjoy life,<br>enjoy the good wine with us.</h1>
  <p class="abs hero-sub">We hope to see you soon - Margaret Zhou</p>
  <div class="abs hero-cta pill">Integrations <span class="dot"><svg width="8" height="8" viewBox="0 0 8 8"><path d="M1 4h6M4.5 1.5L7 4 4.5 6.5" stroke="#fff" fill="none"/></svg></span></div>
</section>

<div class="abs center eyebrow" style="top:670px">Discover</div>
<h2 class="abs center heading section-title" style="top:690px">Our Top Wines<div class="title-rule"></div></h2>
<section class="abs wine-band">
  <div class="wine-feature"><div class="feature-slot" role="img" aria-label="Red wine bottle photo"></div></div>
  <div class="wine-panel"><div class="bottle-slot" role="img" aria-label="White wine bottle photo"></div><div class="panel-label">WHITE WINE<small>SHOP NOW</small></div></div>
  <div class="wine-panel"><div class="bottle-slot" role="img" aria-label="Rose wine bottle photo"></div><div class="panel-label">ROSE STYLE WINE<small>SHOP NOW</small></div></div>
  <div class="wine-panel"><div class="bottle-slot" role="img" aria-label="Sparkling wine bottle photo"></div><div class="panel-label">SPARKLING &amp; CHAMPAGNE WINE<small>SHOP NOW</small></div></div>
  <div class="wine-panel"><div class="bottle-slot" role="img" aria-label="Red wine bottle photo"></div><div class="panel-label">RED WINE<small>SHOP NOW</small></div></div>
</section>
<div class="abs arrow-btn filled" style="left:566px;top:1125px"><svg width="8" height="8" viewBox="0 0 8 8"><path d="M5.5 1L2.5 4l3 3" stroke="#fff" fill="none" stroke-width="1.5"/></svg></div>
<div class="abs arrow-btn" style="left:606px;top:1125px"><svg width="8" height="8" viewBox="0 0 8 8"><path d="M2.5 1l3 3-3 3" stroke="#1a6fb5" fill="none" stroke-width="1.5"/></svg></div>

<section class="abs about">
  <div class="abs about-photo" role="img" aria-label="Photo of a smiling woman tasting a glass of white wine"></div>
  <div class="abs eyebrow" style="left:162px;top:76px;text-transform:none;letter-spacing:.5px">Who We Are</div>
  <h2 class="abs heading section-title" style="left:162px;top:94px;font-size:24px">About Us</h2>
  <p class="abs about-text">Lanmeixo is a wine company that was founded by several wine lovers, including Margaret Zhou and close friends, in March 2016. The company is based in Perth, Western Australia and was set up to bring fine Australian wine to China. Over past three years we have travelled and visited many celebrated wine regions across the country, including Margaret River and the Swan Valley. We have built honest friendships and lasting partnerships with many family owned wineries and wine makers, and we remain committed to excellence and to quality of product.</p>
  <div class="abs goal" style="left:162px;top:282px">
    <div class="goal-icon"><svg width="22" height="22" viewBox="0 0 22 22"><circle cx="11" cy="11" r="8" stroke="#7b8794" fill="none"/><circle cx="11" cy="11" r="4" stroke="#7b8794" fill="none"/><circle cx="11" cy="11" r="1.3" fill="#7b8794"/></svg></div>
    <h4>Lanmeixo's Mission:</h4>
    <p>To Be Your Most Trustworthy And Responsible Wine Provider. Share All Our Passion For Individuals And Businesses.</p>
  </div>
  <div class="abs goal" style="left:535px;top:282px">
    <div class="goal-icon"><svg width="22" height="22" viewBox="0 0 22 22"><path d="M2 11c3-5 15-5 18 0-3 5-15 5-18 0z" stroke="#7b8794" fill="none"/><circle cx="11" cy="11" r="3" stroke="#7b8794" fill="none"/></svg></div>
    <h4>Lanmeixo's Vision:</h4>
    <p>Ensure The Best Premium Wines Reach Our Clients In China, Providing Real Value To Every Customer And Partner.</p>
  </div>
  <div class="abs pill" style="left:162px;top:418px;border:1px solid #cfe0ec">Know More About Us <span class="dot"><svg width="8" height="8" viewBox="0 0 8 8"><path d="M1 4h6M4.5 1.5L7 4 4.5 6.5" stroke="#fff" fill="none"/></svg></span></div>
</section>

<div class="abs center eyebrow" style="top:1822px">Tastefully Yours</div>
<h2 class="abs center heading section-title" style="top:1842px">Shop Extract<div class="title-rule"></div></h2>
<div class="abs filter" style="left:353px;top:1902px;border-color:#c4c9ce">All</div>
<div class="abs filter" style="left:460px;top:1902px;border-color:#7a1a2a">Red<br>Wine</div>
<div class="abs filter" style="left:567px;top:1902px;border-color:#c4c9ce">White<br>Wine</div>
<div class="abs filter" style="left:683px;top:1902px;border-color:#e06c95">Rose Style<br>Wine</div>
<div class="abs filter" style="left:772px;top:1902px;border-color:#4bb36b">Sparkling &amp;<br>Champagne<br>Wine</div>

<div class="abs product hover" style="left:162px;top:1990px">
  <div class="product-shot" style="background:linear-gradient(90deg,#3e0e18,#8a2838 45%,#4a1320)" role="img" aria-label="Red wine bottle photo"></div>
  <span class="badge" style="background:#2b3440">NEW</span>
  <div class="product-name" style="color:var(--blue)">Red Wine</div>
  <div class="product-price">$30.00</div>
  <div class="stars">★★★★<span class="off">★</span></div>
</div>
<div class="abs product" style="left:386px;top:1990px">
  <div class="product-shot" style="background:linear-gradient(90deg,#1c1916,#4a443d 45%,#24201c)" role="img" aria-label="White wine bottle photo"></div>
  <span class="badge" style="background:var(--blue)">SALE</span>
  <div class="product-name">White Wine</div>
  <div class="product-price">$30.00</div>
  <div class="stars">★★★★<span class="off">★</span></div>
</div>
<div class="abs product" style="left:607px;top:1990px">
  <div class="product-shot" style="background:linear-gradient(90deg,#5a1024,#b03456 45%,#6a1530)" role="img" aria-label="Rose style wine bottle photo"></div>
  <div class="product-name">Rose Style Wine</div>
  <div class="product-price">$30.00</div>
  <div class="stars">★★★★<span class="off">★</span></div>
</div>
<div class="abs product" style="left:826px;top:1990px">
  <div class="product-shot" style="background:linear-gradient(90deg,#a82424,#f06060 45%,#b82a2a)" role="img" aria-label="Sparkling wine bottle photo"></div>
  <div class="product-name">Sparkling &amp; Champagne Wine</div>
  <div class="product-price">$30.00</div>
  <div class="stars">★★★★<span class="off">★</span></div>
</div>

<section class="abs team">
  <div class="abs eyebrow" style="left:162px;top:60px;color:#ffffff">Team</div>
  <h2 class="abs heading" style="left:162px;top:82px;font-size:26px;color:#ffffff">Members in Team</h2>
  <div class="abs round-arrow" style="left:938px;top:86px;border:1px solid #ffffff"><svg width="8" height="8" viewBox="0 0 8 8"><path d="M5.5 1L2.5 4l3 3" stroke="#fff" fill="none" stroke-width="1.5"/></svg></div>
  <div class="abs round-arrow" style="left:993px;top:86px;background:#ffffff"><svg width="8" height="8" viewBox="0 0 8 8"><path d="M2.5 1l3 3-3 3" stroke="#1da1e2" fill="none" stroke-width="1.5"/></svg></div>
  <div class="abs member" style="left:162px;top:162px"><div class="member-photo" role="img" aria-label="Team member portrait"></div><div class="member-name">Member Name</div><div class="member-role">POSITION</div></div>
  <div class="abs member" style="left:383px;top:162px"><div class="member-photo" role="img" aria-label="Team member portrait"></div><div class="member-name">Member Name</div><div class="member-role">POSITION</div></div>
  <div class="abs member" style="left:612px;top:162px"><div class="member-photo" role="img" aria-label="Team member portrait"></div><div class="member-name">Member Name</div><div class="member-role">POSITION</div></div>
  <div class="abs member" style="left:833px;top:162px"><div class="member-photo" role="img" aria-label="Team member portrait"></div><div class="member-name">Member Name</div><div class="member-role">POSITION</div></div>
</section>

<div class="abs center eyebrow" style="top:2946px">Blog Post</div>
<h2 class="abs center heading section-title" style="top:2966px">Blogs &amp; News<div class="title-rule"></div></h2>
<article class="abs blog" style="left:162px;top:3092px">
  <div class="blog-img" role="img" aria-label="Photo of wine bottles lined up on a bar"></div>
  <div class="blog-caption">Duis aute irure dolor in reprehenderit in voluptate velit</div>
  <div class="blog-meta"><span>May 30, 2019</span><span>0 Comments</span></div>
</article>
<article class="abs blog" style="left:462px;top:3092px">
  <div class="blog-img" role="img" aria-label="Photo of wine bottles lined up on a bar"></div>
  <div class="blog-title">Duis aute irure dolor in reprehenderit in voluptate velit</div>
  <div class="blog-meta"><span>May 30, 2019</span><span>0 Comments</span></div>
</article>
<article class="abs blog" style="left:762px;top:3092px">
  <div class="blog-img" role="img" aria-label="Photo of wine bottles lined up on a bar"></div>
  <div class="blog-title">Duis aute irure dolor in reprehenderit in voluptate velit</div>
  <div class="blog-meta"><span>May 30, 2019</span><span>0 Comments</span></div>
</article>
<div class="abs" style="left:162px;top:3404px;width:876px;height:2px;background:#e3e8ec"></div>
<div class="abs" style="left:162px;top:3404px;width:290px;height:2px;background:var(--blue)"></div>
<div class="abs" style="left:394px;top:3400px;width:10px;height:10px;border-radius:50%;background:#ffffff;border:1px solid #c4ccd3"></div>

<section class="abs affiliate">
  <p>By Joining our Affiliate Program you can upload our banners or product links to any of your social media platforms which may include your Talkora, Qinlu, Streamly channel, blog or website and receive a commission for every sale.</p>
  <div class="btn">Click to Join Our Affiliate Program <span class="pill" style="padding:0"><span class="dot"><svg width="8" height="8" viewBox="0 0 8 8"><path d="M1 4h6M4.5 1.5L7 4 4.5 6.5" stroke="#fff" fill="none"/></svg></span></span></div>
</section>

<div class="abs center eyebrow" style="top:3694px">Have Any Question?</div>
<h2 class="abs center heading section-title" style="top:3712px;font-size:24px">Contact Us</h2>
<div class="abs map" role="img" aria-label="Street map of Perth, Western Australia with the office location pinned"></div>
<section class="abs office">
  <h3>Western Australia, <span>Perth</span></h3>
  <div class="label" style="top:208px">Address</div>
  <div class="line" style="top:226px">Level 4, 120 Harbour Lane<br>Perth, Western Australia</div>
  <div class="label" style="top:262px">Phone Number</div>
  <div class="line" style="top:282px">+61 8 5550 0142 &nbsp;&nbsp;&nbsp; +61 8 5550 0178</div>
  <div class="socials"><span>Talkora</span><span>Qinlu</span><span>Streamly</span><span>Snapvista</span></div>
  <div class="line" style="top:384px;text-decoration:underline">hello@lanmeixo.example</div>
</section>
<form class="abs contact-card">
  <p class="intro">If you want to know any other different wine and brands, please leave a<br>message to us or contact us!</p>
  <div class="field" style="left:30px;top:119px;width:282px">First Name</div>
  <div class="field" style="left:324px;top:119px;width:285px">Last Name</div>
  <div class="field" style="left:30px;top:169px;width:282px">Email</div>
  <div class="field" style="left:324px;top:169px;width:285px">Phone</div>
  <div class="field" style="left:30px;top:209px;width:579px;height:82px">Type Message</div>
  <div class="captcha"><i></i><b></b></div>
  <div class="submit">SUBMIT</div>
</form>

<footer class="abs copyright">Copyright © 2019 Lanmeixo. All Rights Reserved.</footer>

</body>
</html>
```